New Business Card Needed

I need a new business card for Willowmere Kitchen & Bath.
Logo is attached as well a my photo. Note: Make the logo Navy Blue.
Here is the text:
Desmond Ferrick
GC/Owner
Larkston NC
704-555-0183
desmond@willowmereKB.example
www.willowmereKB.example
Tag line on card: BEAUTY | FUNCTION | ON TIME | ON BUDGET
Trim size: 2.56" X 2.56"
This is where we aim to cut the cards.
Safe area: 2.4" X 2.4"
Make sure any important aspects of your design such as text and logos are inside of the safe area, otherwise they may be cut off.
Bleed area: 2.71 X 2.71
Make sure that your background extends to fill the bleed to avoid your Business Cards having white edges when trimmed.
On the back side. Use photo of kitchen attached.

```html
<!DOCTYPE html>
<html lang="en">
<head>
<meta charset="utf-8">
<title>Willowmere Kitchen &amp; Bath — Business Card</title>
<link href="https://fonts.googleapis.com/css2?family=Montserrat:wght@400;500;600;700&display=swap" rel="stylesheet">
<style>
  :root {
    --navy: #0f2350;
    --navy-deep: #0c1f4a;
    --sky: #27a9e8;
    --white: #ffffff;
    --stage: #3d3d3f;
    --wood-light: #d9b98a;
    --wood-mid: #b98a58;
    --kitchen-white: #ecebe6;
  }
  * { box-sizing: border-box; margin: 0; padding: 0; }
  html, body { width: 1200px; height: 1200px; overflow: hidden; }
  body {
    background: var(--stage);
    font-family: "Montserrat", sans-serif;
    position: relative;
  }
  .card {
    position: absolute;
    width: 520px;
    height: 520px;
    overflow: hidden;
    box-shadow: 0 10px 30px rgba(0,0,0,0.45);
  }
  /* Front */
  .card-front { left: 70px; top: 70px; background: var(--white); }
  .front-brand {
    height: 178px;
    display: flex;
    align-items: center;
    justify-content: center;
    gap: 14px;
  }
  .brand-mark {
    width: 22px; height: 22px;
    background: var(--navy);
    flex: none;
  }
  .brand-name {
    font-weight: 600;
    font-size: 29px;
    letter-spacing: 0.5px;
    color: var(--navy);
    white-space: nowrap;
  }
  .tagline-band {
    height: 40px;
    background: var(--navy);
    color: var(--white);
    font-weight: 600;
    font-size: 16px;
    letter-spacing: 0.3px;
    display: flex;
    align-items: center;
    justify-content: center;
  }
  .kitchen-photo {
    height: 302px;
    background: linear-gradient(160deg, var(--kitchen-white) 0%, var(--wood-light) 45%, var(--kitchen-white) 70%, var(--wood-mid) 100%);
  }
  /* Back */
  .card-back { left: 610px; top: 610px; background: var(--navy-deep); color: var(--white); }
  .back-brand {
    position: absolute;
    top: 95px; left: 0; right: 0;
    display: flex;
    align-items: center;
    justify-content: center;
    gap: 14px;
  }
  .back-brand .brand-mark { background: var(--white); }
  .back-brand .brand-name { color: var(--white); }
  .portrait {
    position: absolute;
    left: 40px; top: 285px;
    width: 190px; height: 190px;
    border: 2px solid var(--sky);
    background: linear-gradient(160deg, #3a3c42 0%, #25272c 100%);
  }
  .contact {
    position: absolute;
    left: 250px; top: 268px;
    width: 245px;
  }
  .person-name {
    font-weight: 500;
    font-size: 21px;
    color: var(--sky);
    letter-spacing: 0.3px;
    white-space: nowrap;
  }
  .person-title {
    font-weight: 500;
    font-size: 14px;
    margin-top: 2px;
    margin-bottom: 14px;
  }
  .contact-list { list-style: none; }
  .contact-list li {
    display: flex;
    align-items: center;
    gap: 8px;
    font-size: 13px;
    margin-bottom: 8px;
    white-space: nowrap;
  }
  .contact-list svg { width: 15px; height: 15px; flex: none; }
</style>
</head>
<body>

  <section class="card card-front">
    <div class="front-brand">
      <span class="brand-mark"></span>
      <span class="brand-name">Willowmere Kitchen &amp; Bath</span>
    </div>
    <div class="tagline-band">BEAUTY | FUNCTION | ON TIME | ON BUDGET</div>
    <div class="kitchen-photo" role="img" aria-label="Photo of a bright remodeled kitchen with wood cabinets, white island and bar stools"></div>
  </section>

  <section class="card card-back">
    <div class="back-brand">
      <span class="brand-mark"></span>
      <span class="brand-name">Willowmere Kitchen &amp; Bath</span>
    </div>

    <div class="portrait" role="img" aria-label="Portrait photo of the owner"></div>

    <div class="contact">
      <p class="person-name">DESMOND FERRICK</p>
      <p class="person-title">GC/OWNER</p>
      <ul class="contact-list">
        <li>
          <svg viewBox="0 0 24 24" fill="var(--sky)"><path d="M6.6 10.8a15.1 15.1 0 0 0 6.6 6.6l2.2-2.2a1 1 0 0 1 1-.25 11.4 11.4 0 0 0 3.6.57 1 1 0 0 1 1 1V20a1 1 0 0 1-1 1A17 17 0 0 1 3 4a1 1 0 0 1 1-1h3.5a1 1 0 0 1 1 1c0 1.25.2 2.45.57 3.57a1 1 0 0 1-.25 1z"/></svg>
          704-555-0183
        </li>
        <li>
          <svg viewBox="0 0 24 24" fill="none" stroke="var(--sky)" stroke-width="2"><circle cx="12" cy="12" r="9"/><path d="M3 12h18M12 3c3 3.5 3 14.5 0 18M12 3c-3 3.5-3 14.5 0 18"/></svg>
          www.willowmereKB.example
        </li>
        <li>
          <svg viewBox="0 0 24 24" fill="none" stroke="var(--sky)" stroke-width="2"><rect x="3" y="5" width="18" height="14"/><path d="M3 5l9 8 9-8"/></svg>
          desmond@willowmereKB.example
        </li>
        <li>
          <svg viewBox="0 0 24 24" fill="none" stroke="var(--sky)" stroke-width="2"><path d="M12 22s7-7 7-12a7 7 0 0 0-14 0c0 5 7 12 7 12z"/><circle cx="12" cy="10" r="2.5"/></svg>
          Larkston NC
        </li>
      </ul>
    </div>
  </section>

</body>
</html>
```